Corvenne Jewelers Business Cards

A creative, cool edgy business card for our entire team that says we are a young, hip, luxury jewelry store specializing in diamonds and engagement rings but that we are also personal shoppers and trusted advisors. Our colors are Navy Blue & Platinum

I have included our past business card.

Font styles to use
Serif

Colors
0255a3

Requirements
Nice to have
• A card stock that you can write on with a pen

```html
<!DOCTYPE html>
<html lang="en">
<head>
<meta charset="utf-8">
<title>Corvenne Jewelers Business Cards</title>
<link href="https://fonts.googleapis.com/css2?family=Cinzel:wght@400&family=EB+Garamond:wght@400&family=Marcellus&display=swap" rel="stylesheet">
<style>
  :root {
    --navy: #1a2460;
    --navy-deep: #152058;
    --platinum: #d8dbe4;
    --paper: #ffffff;
    --backdrop: #000000;
  }
  * { margin: 0; padding: 0; box-sizing: border-box; }
  html, body { width: 1200px; height: 1200px; overflow: hidden; background: var(--backdrop); }
  .sheet { position: relative; width: 1200px; height: 1200px; }

  .card { position: absolute; background: var(--paper); overflow: hidden; }
  .card-front { left: 96px; top: 28px; width: 1010px; height: 562px; }
  .card-back { left: 94px; top: 600px; width: 1012px; height: 574px; }

  .front-glow {
    position: absolute; inset: 0;
    background:
      radial-gradient(ellipse 340px 300px at 0px 300px, #3a4277 0%, #7d83a6 35%, rgba(200,203,218,0.7) 70%, rgba(255,255,255,0) 100%),
      radial-gradient(ellipse 700px 420px at 260px 300px, #e3e4ec 0%, #f2f2f6 55%, rgba(255,255,255,0) 100%),
      var(--paper);
  }
  .gem-visual {
    position: absolute; left: 0; top: 152px; width: 590px; height: 332px;
    background:
      radial-gradient(ellipse 240px 140px at 110px 160px, #4a545e 0%, #6c7781 45%, rgba(140,148,160,0.5) 75%, rgba(200,205,215,0) 100%),
      radial-gradient(ellipse 220px 130px at 380px 160px, rgba(150,155,165,0.5) 0%, rgba(220,222,230,0) 100%);
  }

  .brand-title {
    position: absolute; text-align: center; line-height: 1;
    font-family: "Cinzel", serif; color: var(--navy); font-weight: 400;
  }
  .card-front .brand-title { top: 30px; left: 100px; width: 872px; font-size: 66px; letter-spacing: 1px; }

  .contact { position: absolute; left: 512px; top: 0; width: 440px; height: 100%; text-align: center; color: var(--navy); font-family: "EB Garamond", serif; }
  .contact p { position: absolute; left: 0; right: 0; line-height: 1; }
  .salesperson { top: 149px; font-size: 30px; }
  .store-info { top: 191px; font-size: 38px; font-family: "Marcellus", serif; }
  .phone { top: 234px; font-size: 30px; }
  .street { top: 347px; font-size: 30px; }
  .city { top: 385px; font-size: 30px; }
  .extra { top: 440px; font-size: 26px; }

  .front-mark {
    position: absolute; left: 846px; top: 392px; width: 150px; text-align: center;
    font-family: "Cinzel", serif; color: var(--navy); font-size: 16px; line-height: 1.2;
  }
  .front-mark svg { display: block; margin: 0 auto 8px; }

  .back-mark { position: absolute; left: 406px; top: 50px; }
  .card-back .brand-title { top: 344px; left: 0; right: 0; font-size: 48px; letter-spacing: 0.5px; }

  .hours-band {
    position: absolute; left: 0; right: 0; top: 410px; bottom: 0;
    background: var(--navy-deep); color: var(--paper); text-align: center;
  }
  .hours-band p { position: absolute; left: 0; right: 0; line-height: 1; }
  .hours-title { top: 7px; font-family: "Marcellus", serif; font-size: 40px; }
  .hours-line { font-family: "EB Garamond", serif; font-size: 36px; }
  .hours-weekday { top: 58px; }
  .hours-weekend { top: 96px; }
</style>
</head>
<body>
<div class="sheet">

  <section class="card card-front">
    <div class="front-glow"></div>
    <div class="gem-visual" role="img" aria-label="Photograph of a faceted diamond dissolving into sparkling fragments"></div>
    <h1 class="brand-title">Corvenne Jewelers</h1>
    <div class="contact">
      <p class="salesperson">Salesperson Name</p>
      <p class="store-info">Store Information</p>
      <p class="phone">555.123.4567</p>
      <p class="street">5555 Adresss Road</p>
      <p class="city">City, State, Zip</p>
      <p class="extra">Additional Info</p>
    </div>
    <div class="front-mark">
      <svg width="86" height="86" viewBox="0 0 86 86" aria-hidden="true">
        <circle cx="43" cy="43" r="39" fill="none" stroke="var(--navy)" stroke-width="4"/>
      </svg>
      Corvenne Jewelers
    </div>
  </section>

  <section class="card card-back">
    <svg class="back-mark" width="200" height="200" viewBox="0 0 200 200" aria-hidden="true">
      <circle cx="100" cy="100" r="92" fill="none" stroke="var(--navy)" stroke-width="8"/>
    </svg>
    <h2 class="brand-title">Corvenne Jewelers</h2>
    <div class="hours-band">
      <p class="hours-title">Store Hours</p>
      <p class="hours-line hours-weekday">Monday - Friday: 9am - 7:00pm</p>
      <p class="hours-line hours-weekend">Saturday &amp; Sunday: 11am - 5pm</p>
    </div>
  </section>

</div>
</body>
</html>
```